Kestrel Signs Facebook Banner Design

Design a facebook banner for a sign company. I would like to have a modern approach to it.

Product Offering:
Signs
Banners
Decals
Commercial Wraps

```html
<!DOCTYPE html>
<html lang="en">
<head>
<meta charset="utf-8">
<title>Kestrel Signs – Facebook Cover</title>
<link href="https://fonts.googleapis.com/css2?family=Poppins:ital,wght@0,700;0,800;0,900;1,900&display=swap" rel="stylesheet">
<style>
  :root {
    --stage: #13337a;
    --paper: #ffffff;
    --brand-red: #e8161d;
    --ink-dark: #3a3a3a;
    --ink-black: #111111;
    --card-grey: #4a4a4c;
    --on-red: #ffffff;
  }
  html, body {
    margin: 0;
    padding: 0;
    width: 1200px;
    height: 987px;
    overflow: hidden;
    background: var(--stage);
  }
  .cover {
    position: absolute;
    left: 50px;
    top: 290px;
    width: 1100px;
    height: 407px;
    display: block;
    background: var(--paper);
  }
  .cover text { font-family: "Poppins", sans-serif; }
  .headline-lead { font-weight: 800; fill: var(--ink-dark); }
  .brand-name { font-weight: 900; font-style: italic; }
  .brand-accent { fill: var(--brand-red); }
  .brand-dark { fill: var(--ink-dark); }
  .services-title { font-weight: 700; fill: var(--ink-black); }
  .services-title .accent { fill: var(--brand-red); }
  .card-red { fill: var(--brand-red); }
  .card-grey { fill: var(--card-grey); }
  .card-label { font-weight: 800; fill: var(--on-red); }
  .phone { font-weight: 800; fill: var(--brand-red); }
  .website { font-weight: 800; fill: var(--ink-dark); }
  .badge { fill: var(--brand-red); }
  .badge-text { font-weight: 900; fill: var(--on-red); }
  .accent-band { fill: var(--brand-red); }
</style>
</head>
<body>
<svg class="cover" viewBox="0 0 1655 613" xmlns="http://www.w3.org/2000/svg" aria-label="Kestrel Signs cover">
  <defs>
    <linearGradient id="photo-workshop" x1="0" y1="0" x2="1" y2="1">
      <stop offset="0" stop-color="#e6e8ea"/>
      <stop offset="0.35" stop-color="#6f87a8"/>
      <stop offset="0.65" stop-color="#3e4f3a"/>
      <stop offset="1" stop-color="#8b8e92"/>
    </linearGradient>
    <linearGradient id="photo-signs" x1="0" y1="0" x2="0" y2="1">
      <stop offset="0" stop-color="#9aa6ae"/>
      <stop offset="1" stop-color="#3f5a3a"/>
    </linearGradient>
    <linearGradient id="photo-banners" x1="0" y1="0" x2="1" y2="1">
      <stop offset="0" stop-color="#cfd3d6"/>
      <stop offset="1" stop-color="#8c9296"/>
    </linearGradient>
    <linearGradient id="photo-decals" x1="0" y1="0" x2="1" y2="1">
      <stop offset="0" stop-color="#7a5a4a"/>
      <stop offset="1" stop-color="#c9b8a6"/>
    </linearGradient>
    <linearGradient id="photo-wraps" x1="0" y1="0" x2="0" y2="1">
      <stop offset="0" stop-color="#8cc4e8"/>
      <stop offset="1" stop-color="#2a8fb0"/>
    </linearGradient>
  </defs>

  <!-- headline -->
  <text class="headline-lead" x="74" y="95" font-size="60" textLength="777" lengthAdjust="spacingAndGlyphs">TRANSFORM YOUR BRAND WITH</text>
  <text class="brand-name brand-accent" x="74" y="166" font-size="82" textLength="490" lengthAdjust="spacingAndGlyphs">KESTREL</text>
  <text class="brand-name brand-dark" x="582" y="166" font-size="82" textLength="262" lengthAdjust="spacingAndGlyphs">SIGNS</text>

  <!-- services -->
  <text class="services-title" x="109" y="243" font-size="48" textLength="300" lengthAdjust="spacingAndGlyphs">OUR <tspan class="accent">SERVICES</tspan></text>

  <g class="service-card">
    <path class="card-red" d="M101 255 L279 255 L236 450 L56 450 Z" stroke="#e8161d" stroke-width="8" stroke-linejoin="round"/>
    <path role="img" aria-label="Photo collage of storefront and pylon signs" fill="url(#photo-signs)" d="M109 265 L267 265 L238 390 L80 390 Z"/>
    <text class="card-label" x="151" y="432" font-size="26" text-anchor="middle">SIGNS</text>
  </g>
  <g class="service-card" transform="translate(193 0)">
    <path class="card-grey" d="M101 255 L279 255 L236 450 L56 450 Z" stroke="#4a4a4c" stroke-width="8" stroke-linejoin="round"/>
    <path role="img" aria-label="Photo of roll-up and flag banners" fill="url(#photo-banners)" d="M109 265 L267 265 L238 390 L80 390 Z"/>
    <text class="card-label" x="151" y="430" font-size="26" text-anchor="middle">BANNERS</text>
  </g>
  <g class="service-card" transform="translate(386 0)">
    <path class="card-red" d="M101 255 L279 255 L236 450 L56 450 Z" stroke="#e8161d" stroke-width="8" stroke-linejoin="round"/>
    <path role="img" aria-label="Photo of printed sticker decals in hand" fill="url(#photo-decals)" d="M109 265 L267 265 L238 390 L80 390 Z"/>
    <text class="card-label" x="151" y="432" font-size="26" text-anchor="middle">DECALS</text>
  </g>
  <g class="service-card" transform="translate(579 0)">
    <path class="card-grey" d="M101 255 L279 255 L236 450 L56 450 Z" stroke="#4a4a4c" stroke-width="8" stroke-linejoin="round"/>
    <path role="img" aria-label="Photo of a pickup truck with a blue vinyl wrap" fill="url(#photo-wraps)" d="M109 265 L267 265 L238 390 L80 390 Z"/>
    <text class="card-label" x="151" y="418" font-size="22" text-anchor="middle">COMMERCIALS</text>
    <text class="card-label" x="151" y="442" font-size="22" text-anchor="middle">WRAPS</text>
  </g>

  <!-- contact -->
  <text class="phone" x="339" y="540" font-size="76" textLength="429" lengthAdjust="spacingAndGlyphs">(604) 555-0182</text>
  <text class="website" x="341" y="578" font-size="38" textLength="422" lengthAdjust="spacingAndGlyphs">WWW.KESTRELSIGNS.CA</text>

  <!-- photo side -->
  <path class="accent-band" d="M1232 0 L1655 0 L1655 613 L1150 613 L1000 250 Q 975 150 1060 75 Q 1130 25 1232 0 Z"/>

  <g class="experience-badge">
    <rect class="badge" x="801" y="472" width="400" height="118" rx="20"/>
    <text class="badge-text" x="832" y="577" font-size="122" textLength="80" lengthAdjust="spacingAndGlyphs">5</text>
    <text class="badge-text" x="904" y="543" font-size="68" textLength="212" lengthAdjust="spacingAndGlyphs">YEARS</text>
    <text class="badge-text" x="904" y="577" font-size="40" textLength="210" lengthAdjust="spacingAndGlyphs">EXPERIENCE</text>
  </g>

  <path role="img" aria-label="Photo of two print workers in aprons working at a press" fill="url(#photo-workshop)" d="M1110 0 L1655 0 L1655 613 L1165 613 L1040 255 Q 1020 170 1050 95 Q 1070 30 1110 0 Z"/>
</svg>
</body>
</html>
```